Landscape Contractor in need of New Web Design

HELP.. Please Help!!!!. Our current website is old, outdated, ugly... and well nothing like us.... so we are looking for someone to help build a new website that fits our company direction. We are a landscape company with multiple locations in order to meet the needs of our clients and their projects throughout the midwest. When most people think of landscaping, they think of mowing grandmas yard, but that is NOT even remotely close to what we do. We are 100% a commercial landscape company meaning we complete landscape and irrigation services for large scale commercial projects. We are looking for a website to showcase our commercial talents and awesome team of people.
Updates

Address of current website is www.plovermeadowco.com

```html
<!DOCTYPE html>
<html lang="en">
<head>
<meta charset="utf-8">
<title>Plover Meadow Co. — Landscape and Irrigation</title>
<link href="https://fonts.googleapis.com/css2?family=Lato:wght@300;400;700&display=swap" rel="stylesheet">
<style>
:root{
  --lime:#b8f40c;
  --ink:#1c1c1c;
  --text:#333333;
  --muted:#6b6b6b;
  --olive:#4f6532;
  --olive-dark:#3c4d27;
  --charcoal:#343434;
  --footer:#262626;
  --white:#ffffff;
  --line:#2a2a2a;
}
*{margin:0;padding:0;box-sizing:border-box}
html,body{width:1200px;height:5343px;overflow:hidden}
body{position:relative;background:var(--white);font-family:"Lato",sans-serif;color:var(--text)}
.abs{position:absolute}
.photo{position:absolute}
.label{position:absolute;font-size:9px;letter-spacing:1.6px;text-transform:uppercase;color:var(--muted);font-weight:700}

/* header */
.brand-block{left:0;top:0;width:245px;height:108px;background:var(--lime);display:flex;align-items:center;justify-content:center;gap:10px}
.brand-dot{width:18px;height:18px;border-radius:50%;background:var(--ink)}
.brand-name{font-size:20px;font-weight:700;color:var(--ink)}
.nav{left:305px;top:48px;display:flex;gap:24px;font-size:12px;color:var(--ink)}
.contact-info{left:746px;top:42px;font-size:9.5px;line-height:17px;color:var(--muted);font-weight:700}
.btn-pay{left:1030px;top:24px;width:106px;height:28px;background:var(--lime);font-size:9.5px;font-weight:700;color:var(--ink);display:flex;align-items:center;justify-content:center}
.btn-quote{left:1030px;top:58px;width:92px;height:28px;background:var(--ink);font-size:9.5px;font-weight:700;color:var(--white);display:flex;align-items:center;justify-content:center}

/* hero */
.hero-photo{left:0;top:108px;width:1200px;height:613px;background:linear-gradient(180deg,#3f5a2a 0%,#5d7f34 40%,#7ea83c 75%,#6c9233 100%)}
.hero-arrows{left:752px;top:683px;display:flex;gap:2px}
.hero-arrow{width:40px;height:38px;background:var(--lime);display:flex;align-items:center;justify-content:center}
.hero-card{left:852px;top:481px;width:348px;height:365px;background:var(--lime);padding:90px 0 0 40px}
.hero-card .kicker{font-size:9px;font-weight:700;letter-spacing:1px;color:var(--ink)}
.hero-card h1{font-size:25px;font-weight:300;line-height:31px;color:var(--ink);margin-top:18px}
.btn-outline-dark{display:inline-flex;align-items:center;justify-content:center;width:120px;height:30px;border:2px solid var(--ink);font-size:8.5px;font-weight:700;letter-spacing:1px;color:var(--ink);margin-top:18px}
.btn-solid-dark{display:flex;align-items:center;justify-content:center;width:98px;height:28px;background:var(--ink);font-size:8.5px;font-weight:700;letter-spacing:1px;color:var(--white);margin-top:12px}

/* intro */
.intro-title{left:317px;top:866px;width:520px;font-size:29px;line-height:39px;font-weight:400;color:var(--ink)}
.intro-title .mark{border-bottom:4px solid var(--lime)}
.intro-copy{left:321px;top:1038px;width:560px;font-size:12.5px;line-height:20.5px;color:var(--muted)}
.read-more{left:323px;top:1136px;font-size:8.5px;font-weight:700;letter-spacing:1.6px;color:var(--muted);display:flex;align-items:center;gap:8px}

/* band */
.band{left:0;top:1308px;width:1200px;height:323px;background:linear-gradient(180deg,var(--olive-dark),var(--olive) 60%,#557137)}
.band-photo{left:305px;top:1217px;width:590px;height:236px;background:linear-gradient(180deg,#8f4a3a 0%,#4b6d2e 35%,#6c9a3a 70%,#b8b0a2 100%)}
.band-text{left:0;top:1480px;width:1200px;text-align:center;font-size:23px;line-height:30px;font-weight:300;color:var(--white)}
.btn-estimate{left:510px;top:1559px;width:141px;height:31px;background:var(--ink);color:var(--white);font-size:8.5px;font-weight:700;letter-spacing:1.2px;display:flex;align-items:center;justify-content:center}

/* services */
.services-title{left:244px;top:1706px;width:450px;font-size:23px;line-height:29.5px;font-weight:400;color:var(--ink)}
.btn-services{left:781px;top:1747px;width:175px;height:32px;border:2px solid var(--ink);font-size:8.5px;font-weight:700;letter-spacing:1px;color:var(--ink);display:flex;align-items:center;justify-content:center;gap:8px}
.tile{position:absolute;overflow:hidden}
.tile span{position:absolute;bottom:22px;font-size:16px;color:var(--white)}

/* why */
.why-frame{left:485px;top:2670px;width:355px;height:427px;border:3px solid var(--ink)}
.why-frame-gap{left:830px;top:2800px;width:20px;height:190px;background:var(--white)}
.circle{position:absolute;border-radius:50%}
.why-text{left:631px;top:2766px;width:290px}
.why-text h3{font-size:13px;font-weight:700;color:var(--ink);margin-top:20px}
.why-text p{font-size:13px;line-height:21px;color:var(--muted);margin-top:12px}
.why-arrows{margin-top:24px;display:flex;align-items:center;gap:6px}

.rule{position:absolute;height:2px;background:var(--line)}

/* testimonials */
.testi-title{left:243px;top:3318px;width:230px;font-size:20.5px;line-height:27.5px;color:var(--ink)}
.testi-rule{left:488px;top:3224px;width:2px;height:325px;background:var(--line)}
.testi-copy{left:522px;top:3272px;width:374px;font-size:12px;line-height:21.3px;color:var(--muted)}
.testi-name{left:524px;top:3468px;font-size:13px;font-weight:700;color:var(--ink)}
.testi-org{left:522px;top:3495px;font-size:9px;font-weight:700;color:var(--muted)}
.dots{left:524px;top:3524px;display:flex;gap:3px}
.dots i{width:7px;height:7px;border-radius:50%;background:var(--lime)}

/* projects */
.projects-title{left:0;top:3660px;width:1200px;text-align:center;font-size:17px;font-weight:700;letter-spacing:2px;color:var(--ink)}
.gallery-tag{left:429px;top:3895px;width:176px;height:166px;background:linear-gradient(180deg,#495a3a,#39472c);display:flex;flex-direction:column;align-items:center;justify-content:center;gap:8px}
.gallery-tag b{font-size:11px;font-weight:400;letter-spacing:1px;color:var(--white)}
.gallery-tag em{font-style:normal;background:var(--lime);color:var(--ink);font-size:6.5px;font-weight:700;padding:4px 9px;letter-spacing:.6px}

/* quote */
.quote-band{left:0;top:4188px;width:1200px;height:792px;background:var(--charcoal)}
.quote-card{left:334px;top:4264px;width:292px;height:282px;background:var(--lime)}
.quote-card .inner{position:absolute;left:10px;top:0;width:272px;height:272px;background:linear-gradient(135deg,#6e9d36 0%,#a6d23f 55%,var(--lime) 80%)}
.quote-card span{position:absolute;right:30px;bottom:62px;font-size:19px;line-height:21px;color:var(--ink);text-align:left}
.frame-white{left:657px;top:4264px;width:295px;height:286px;border:6px solid var(--white)}
.field{position:absolute;left:547px;width:287px;border-bottom:1.5px solid #8a8a8a;font-size:10px;color:#e6e6e6;padding:0 0 12px 8px}
.btn-submit{left:547px;top:4888px;width:125px;height:30px;background:var(--ink);color:var(--white);font-size:9px;font-weight:700;letter-spacing:1.5px;display:flex;align-items:center;justify-content:center}

/* footer */
.footer{left:0;top:4980px;width:1200px;height:363px;background:var(--footer)}
.foot-brand{left:245px;top:5070px;display:flex;align-items:center;gap:8px}
.foot-brand i{width:16px;height:16px;border-radius:50%;background:var(--lime)}
.foot-brand b{font-size:15px;font-weight:700;color:var(--lime)}
.foot-about{left:388px;top:5060px;width:190px;font-size:10px;line-height:17px;color:#9a9a9a}
.foot-phone{left:388px;top:5166px;font-size:9.5px;line-height:15px;color:var(--lime);font-weight:700}
.foot-divider{left:623px;top:5038px;width:1.5px;height:197px;background:#777}
.foot-name{left:680px;top:5060px;font-size:15px;color:#cfcfcf}
.foot-addr{position:absolute;top:5094px;font-size:8px;line-height:16px;color:#9a9a9a}
.foot-hours{left:680px;top:5140px;font-size:13.5px;color:#cfcfcf}
.social{left:682px;top:5182px;display:flex;gap:4px}
.social i{width:21px;height:21px;border-radius:50%}
.foot-rule{left:199px;top:5270px;width:813px;height:1px;background:#777}
.copyright{left:0;top:5294px;width:1200px;text-align:center;font-size:10.5px;color:#cfcfcf}
</style>
</head>
<body>

<!-- header -->
<div class="abs brand-block"><i class="brand-dot"></i><span class="brand-name">plover meadow</span></div>
<nav class="abs nav"><span>Home</span><span>About us</span><span>Divisions</span><span>Services</span><span>Gallery</span><span>Contact us</span></nav>
<div class="abs contact-info">Phone Number: (913) 555-0148 &nbsp;|&nbsp; (785) 555-0192<br>Business Hours: 8am - 5pm : Mon - Fri</div>
<div class="abs btn-pay">Make a Payment</div>
<div class="abs btn-quote">Get A Quote</div>

<!-- hero -->
<div class="photo hero-photo" role="img" aria-label="Manicured garden lawn with flower beds, stones and shrubs in front of a house"></div>
<div class="abs hero-arrows">
  <div class="hero-arrow"><svg width="24" height="10" viewBox="0 0 24 10"><path d="M23 5H2M6 1L2 5l4 4" fill="none" stroke="#3d4a12" stroke-width="1.3"/></svg></div>
  <div class="hero-arrow"><svg width="24" height="10" viewBox="0 0 24 10"><path d="M1 5h21M18 1l4 4-4 4" fill="none" stroke="#3d4a12" stroke-width="1.3"/></svg></div>
</div>
<div class="abs hero-card">
  <div class="kicker">PLOVER MEADOW CO. LANDSCAPE AND IRRIGATION</div>
  <h1>15 Years of Professional Landscaping</h1>
  <div class="btn-outline-dark">MORE ABOUT US</div>
  <div class="btn-solid-dark">CONTACT US</div>
</div>

<!-- intro -->
<div class="label" style="left:319px;top:842px">Welcome</div>
<h2 class="abs intro-title"><span class="mark">Plover Meadow Co.</span> is a full service lawn and landscape contractor providing design, installation, and maintenance services.</h2>
<p class="abs intro-copy">Founded by Owen Marsh and Peter Lindqvist, Plover Meadow is the premier landscape maintenance and design company based in Olathe, Kansas. Our company's dedication to innovative design projects created some of the most distinguished landscape projects throughout Kansas, Missouri, and Oklahoma.</p>
<div class="abs read-more">READ MORE ABOUT US <svg width="28" height="8" viewBox="0 0 28 8"><path d="M0 4h26M23 1l3 3-3 3" fill="none" stroke="#6b6b6b" stroke-width="1"/></svg></div>

<!-- band -->
<div class="abs band"></div>
<div class="photo band-photo" role="img" aria-label="Curved garden bed with shrubs, mulch and stone edging beside a wooden fence"></div>
<p class="abs band-text">We don't settle for boring landscape.<br>Contact us to discuss your requirements</p>
<div class="abs btn-estimate">GET FREE ESTIMATE</div>

<!-- services -->
<div class="label" style="left:247px;top:1686px">Services</div>
<h2 class="abs services-title">Our company's dedication to innovative design projects created some of the most distinguished landscape projects throughout Kansas, Missouri, and Oklahoma.</h2>
<div class="abs btn-services">VIEW ALL OUR SERVICES <svg width="26" height="8" viewBox="0 0 26 8"><path d="M0 4h24M21 1l3 3-3 3" fill="none" stroke="#1c1c1c" stroke-width="1.2"/></svg></div>

<div class="tile" style="left:0;top:1953px;width:600px;height:323px;background:linear-gradient(160deg,#8fa3a0 0%,#6f9a45 45%,#4f7a2d 100%)" role="img" aria-label="Sprinklers watering a lawn beside stepping stones"><span style="left:60px">Irrigation</span></div>
<div class="tile" style="left:600px;top:1953px;width:600px;height:323px;background:linear-gradient(160deg,#3a4a2a 0%,#6b7a45 45%,#9b8a6a 100%)" role="img" aria-label="Backyard pond with stone path and lit landscaping"><span style="right:96px">Landscaping</span></div>
<div class="tile" style="left:0;top:2276px;width:400px;height:303px;background:linear-gradient(150deg,#5f8a35 0%,#7d6b4a 55%,#5a4a35 100%)" role="img" aria-label="Rolled sod on bare soil"><span style="left:66px">Turf Management</span></div>
<div class="tile" style="left:400px;top:2276px;width:400px;height:303px;background:linear-gradient(180deg,#3f6a22 0%,#4f8a2a 50%,#3f7a22 100%)" role="img" aria-label="Red ride-on mower cutting stripes in a lawn"><span style="left:232px">Maintenance</span></div>
<div class="tile" style="left:800px;top:2276px;width:400px;height:303px;background:linear-gradient(160deg,#2f4a22 0%,#5a6a3a 50%,#7a7a5a 100%)" role="img" aria-label="Stone water feature with patio umbrella and trees"><span style="left:200px">Hardscaping</span></div>

<!-- why choose us -->
<div class="abs why-frame"></div>
<div class="abs why-frame-gap"></div>
<div class="circle" style="left:77px;top:2766px;width:240px;height:240px;background:linear-gradient(135deg,#7a8a4a,#8a7a5a)" role="img" aria-label="Mulch bed with low green plants"></div>
<div class="circle" style="left:265px;top:2705px;width:352px;height:352px;background:linear-gradient(135deg,#4f7a2a,#6f9a3a 60%,#4f7a28)" role="img" aria-label="Close-up of thick green lawn beside stone edging"></div>
<div class="abs why-text">
  <div class="label" style="position:static">Why choose us?</div>
  <h3>05. Free Consultations</h3>
  <p>Call our office to set up a time to meet with one of our qualified professionals. They will walk your property with you to help trouble shoot problems and work to bring your vision to life.</p>
  <div class="why-arrows"><svg width="80" height="26" viewBox="0 0 80 26"><path d="M26 13H2M6 9l-4 4 4 4" fill="none" stroke="#1c1c1c" stroke-width="1.3"/><path d="M44 3L36 23" stroke="#1c1c1c" stroke-width="1.3"/><path d="M54 13h24M74 9l4 4-4 4" fill="none" stroke="#1c1c1c" stroke-width="1.3"/></svg></div>
</div>

<div class="rule" style="left:66px;top:3179px;width:1066px"></div>

<!-- testimonials -->
<div class="label" style="left:247px;top:3282px">Testimonials</div>
<svg class="abs" style="left:326px;top:3262px" width="48" height="40" viewBox="0 0 48 40"><path d="M4 36c0-14 4-24 14-30l2 3c-6 4-8 9-8 13h8v14zM28 36c0-14 4-24 14-30l2 3c-6 4-8 9-8 13h8v14z" fill="#1c1c1c"/></svg>
<h2 class="abs testi-title">We've been fortunate enough to work we some amazing people. Here's what they say about our work.</h2>
<div class="abs testi-rule"></div>
<p class="abs testi-copy">I went by Hollander again this morning and checked the work performed recently. All areas look very nice and it looks like we received more sod north of the playground than I expected, which should make the Principal happy. I am very pleased with the work performed by Plover Meadow and the cooperation from you on the out of your control delays in schedule and revisions to the scope of work. It has been a pleasant experience. Thanks.</p>
<div class="abs testi-name">Dale Hensley</div>
<div class="abs testi-org">- Prairie View School District</div>
<div class="abs dots"><i></i><i></i><i></i></div>

<div class="rule" style="left:39px;top:3592px;width:1068px"></div>

<!-- projects -->
<h2 class="abs projects-title">OUR PROJECTS</h2>
<div class="photo" style="left:243px;top:3717px;width:174px;height:166px;background:linear-gradient(180deg,#9ab0c8 0%,#8a8a6a 45%,#6a7a3a 100%)" role="img" aria-label="Newly laid turf in front of a commercial building"></div>
<div class="photo" style="left:429px;top:3717px;width:176px;height:166px;background:linear-gradient(180deg,#c8c8c0 0%,#7a8a5a 50%,#4a5a3a 100%)" role="img" aria-label="Shrub planting beside a building"></div>
<div class="photo" style="left:616px;top:3717px;width:340px;height:344px;background:linear-gradient(180deg,#a8c0d8 0%,#6a7a4a 30%,#8ab040 70%,#a8c850 100%)" role="img" aria-label="Planted bed with hostas in front of an information center sign"></div>
<div class="photo" style="left:243px;top:3895px;width:174px;height:166px;background:linear-gradient(180deg,#4a8a6a 0%,#6a9a4a 50%,#7aa84a 100%)" role="img" aria-label="Crew rolling a sports field"></div>
<div class="abs gallery-tag" role="img" aria-label="Municipal planting project"><b>MUNICIPALITY</b><em>VIEW GALLERY</em></div>

<!-- quote -->
<div class="abs quote-band"></div>
<div class="photo" style="left:58px;top:4150px;width:419px;height:622px;background:linear-gradient(180deg,#2f4a22 0%,#5a7a35 45%,#8a8a6a 75%,#a8b850 100%)" role="img" aria-label="Woodland stepping stone path lined with hostas"></div>
<div class="abs quote-card"><div class="inner" role="img" aria-label="Bright lawn and plantings beside a house"></div><span>Request a<br>quick quote</span></div>
<div class="photo frame-white" style="background:linear-gradient(180deg,#2f4a22 0%,#4f7a2a 45%,#6a9a35 80%,#7a6a9a 100%)" role="img" aria-label="Shaded lawn with flowering border"></div>

<div class="field" style="top:4648px">Enter Your Name</div>
<div class="field" style="top:4698px">Enter Your Email</div>
<div class="field" style="top:4750px">Snow Removal</div>
<div class="field" style="top:4806px;padding-bottom:46px">Message</div>
<div class="abs btn-submit">SUBMIT</div>

<!-- footer -->
<div class="abs footer"></div>
<div class="abs foot-brand"><i></i><b>plover meadow</b></div>
<p class="abs foot-about">Plover Meadow strives to set the standard for the highest quality lawn and landscape products and services and to exceed our customer's expectations every time.</p>
<div class="abs foot-phone">Phone Number<br>(913) 555-0148 | (785) 555-0192</div>
<div class="abs foot-divider"></div>
<div class="abs foot-name">Plover Meadow Co.</div>
<div class="foot-addr" style="left:680px">4120 W 78th Terrace<br>Lenexa, KS 66227</div>
<div class="foot-addr" style="left:806px">905 Mill Creek Road<br>Junction City, KS 66441</div>
<div class="abs foot-hours">Business Hours: 8am - 5pm : Mon - Fri</div>
<div class="abs social"><i style="background:#3b5998"></i><i style="background:#dd4b39"></i><i style="background:#1da1f2"></i></div>
<div class="abs foot-rule"></div>
<div class="abs copyright">Copyright 2021 Plover Meadow Co. All Rights Reserved.</div>

</body>
</html>
```